Modern HomePage Design for Church

We are looking for a modern homepage design using the sections we put together in the template. The colors we want are blue, black, grey, and white. We do not want use the colors in the logo. Please modify the logo color to match the website color scheme.

Target Market(s)

Church

Industry/Entity Type

Church

Number of Pages Required

1 page

Colors
0293ce
ffffff
474747
9d9d9d

```html
<!DOCTYPE html>
<html lang="en">
<head>
<meta charset="utf-8">
<title>Wellspring Grace Church — Home</title>
<link href="https://fonts.googleapis.com/css2?family=Montserrat:ital,wght@0,400;0,500;0,600;0,700;1,400;1,600&display=swap" rel="stylesheet">
<style>
:root{
  --blue:#0293ce;
  --white:#ffffff;
  --ink:#474747;
  --grey:#9d9d9d;
  --dark:#1f1f1f;
  --darker:#161616;
  --line:#e3e3e3;
  --canvas:#ececec;
}
*{box-sizing:border-box;margin:0;padding:0}
html,body{width:1200px;height:5233px;overflow:hidden}
body{background:var(--canvas);font-family:'Montserrat',sans-serif;color:var(--ink);font-size:15px;line-height:1.55}
.page{width:1130px;margin:0 35px;background:var(--white);height:5233px;position:relative}
a{color:inherit;text-decoration:none}
.btn{display:inline-block;background:var(--blue);color:var(--white);font-size:13px;font-weight:600;letter-spacing:.5px;padding:10px 22px;text-transform:uppercase}
.photo{display:block}

/* hero */
.hero{position:relative;height:715px;color:var(--white);overflow:hidden}
.hero-bg{position:absolute;inset:0;background:radial-gradient(ellipse at 50% 55%,#6f6f6f 0%,#3b3b3b 45%,#111 100%)}
.topnav{position:absolute;top:0;left:0;right:0;height:62px;display:flex;align-items:center;padding:0 42px;background:rgba(0,0,0,.45)}
.topnav ul{list-style:none;display:flex;gap:28px;font-size:13px;font-weight:600}
.topnav li:first-child{color:var(--blue)}
.topnav .btn{margin-left:auto;padding:20px 24px}
.brand{position:absolute;left:42px;top:92px;display:flex;align-items:center;gap:14px}
.brand-dot{width:34px;height:34px;border-radius:50%;background:var(--blue)}
.brand-name{font-size:44px;font-weight:500;line-height:1;letter-spacing:1px}
.brand-sub{font-size:13px;font-weight:500;letter-spacing:1px;margin-top:6px}
.service-times{position:absolute;right:42px;top:92px;display:flex;gap:12px}
.service-times span{background:rgba(160,160,160,.55);font-size:12px;font-weight:600;padding:7px 14px;text-transform:uppercase}
.hero-copy{position:absolute;top:310px;left:0;right:0;text-align:center}
.hero-kicker{font-style:italic;font-weight:600;font-size:28px}
.hero-title{font-size:64px;font-weight:700;letter-spacing:2px;line-height:1.1}
.hero-rule{width:470px;height:2px;background:var(--white);margin:6px auto 10px}
.hero-sub{font-size:24px;font-weight:700;letter-spacing:1px}
.hero-time{font-size:21px;font-weight:700;margin-top:18px}
.hero-copy .btn{margin-top:24px;font-size:15px;padding:12px 30px}

.visitor-bar{height:80px;background:#2b2b2b;color:var(--white);display:flex;align-items:center;justify-content:space-between;padding:0 42px;font-size:16px}
.visitor-bar .btn{background:var(--white);color:var(--ink);border:1px solid var(--grey)}

/* welcome */
.welcome{height:573px;display:flex;padding:78px 42px 0 77px;gap:52px}
.welcome-text{width:586px}
.welcome h2{font-size:44px;font-weight:400;line-height:1.05;color:#6b6b6b}
.welcome h3{font-size:25px;font-weight:700;color:#5a5a5a;margin:6px 0 28px}
.welcome p{font-size:16px;margin-bottom:20px;line-height:1.7}
.signature{font-style:italic;font-weight:600;font-size:30px;color:var(--darker);border-bottom:2px solid var(--darker);display:inline-block;padding-right:40px;margin-top:14px}
.welcome .photo{width:409px;height:418px;background:linear-gradient(135deg,#d6d6d6,#8a8a8a 55%,#5a5a5a)}

/* countdown */
.countdown{height:255px;background:linear-gradient(90deg,#2d2d2d,#444 50%,#2a2a2a);color:var(--white);display:flex;align-items:center;padding:0 70px 0 77px}
.event-head{display:flex;gap:18px;align-items:center}
.event-head h4{font-size:22px;font-weight:500;color:#cfe9f6}
.event-head .date{font-size:19px;color:#ddd}
.event-note{font-size:15px;margin-top:12px;width:420px;color:#ddd}
.timer{margin-left:auto;text-align:center}
.timer-cells{display:flex}
.timer-cells div{width:120px;border-left:1px solid rgba(255,255,255,.3)}
.timer-cells div:first-child{border-left:none}
.timer-cells small{display:block;font-size:13px;letter-spacing:1px;text-transform:uppercase}
.timer-cells b{font-size:42px;font-weight:500;line-height:1.3}
.timer .btn{margin-top:18px}

/* features */
.features{height:373px;display:flex;justify-content:space-around;padding:70px 60px 0;text-align:center}
.feature{width:300px}
.feature svg{height:72px;margin-bottom:18px}
.feature h5{font-size:17px;font-weight:700;text-transform:uppercase;margin-bottom:6px}
.feature p{font-size:15px;line-height:1.45}

/* involved */
.involved{height:482px;display:flex;background:#232323}
.mosaic{width:700px;display:grid;grid-template-columns:202px 105px 200px 193px;grid-template-rows:202px 280px}
.tile{position:relative}
.tile span{position:absolute;left:16px;top:18px;color:var(--white);font-size:12px;font-weight:700;text-transform:uppercase}
.t-kids{background:linear-gradient(135deg,#6d89a6,#3c4f5e)}
.t-out{grid-column:2/4;background:linear-gradient(135deg,#5b5b5b,#2f2f2f)}
.t-teen{background:linear-gradient(135deg,#8c7a66,#4b4038)}
.t-bible{grid-column:1/3;background:linear-gradient(135deg,#494949,#1e1e1e)}
.t-senior{grid-column:3/5;background:linear-gradient(135deg,#7a7a7a,#3d3d3d)}
.t-senior span{left:auto;right:90px;top:auto;bottom:60px}
.t-bible span{top:120px}
.involved-text{padding:150px 40px 0 50px;color:var(--white)}
.involved-text h2{font-size:44px;font-weight:500;margin-bottom:20px}
.involved-text p{font-size:16px;color:#aaa;line-height:1.6}

/* blog */
.blog{height:530px;display:flex;padding:95px 42px 0 77px;gap:50px}
.blog-text{width:538px}
.blog h2{font-size:44px;font-weight:500;color:#333}
.blog time{display:block;color:var(--blue);font-size:15px;margin:22px 0 22px}
.blog h4{color:var(--blue);font-size:19px;font-weight:600;text-transform:uppercase;margin-bottom:4px}
.blog p{font-size:16px;line-height:1.6}
.blog .btn{margin-top:24px}
.blog .photo{width:460px;height:373px;margin-top:-10px;background:radial-gradient(circle at 40% 75%,#f2b24a,#b35a1f 40%,#2c1c14 80%)}

/* pastor */
.pastor{height:517px;background:linear-gradient(90deg,#1b1b1b,#2f2f2f 60%,#1d1d1d);color:var(--white);display:flex;padding:80px 42px 0 42px}
.pastor-col{width:660px}
.label{font-size:20px;font-weight:500;text-transform:uppercase;margin-bottom:22px}
.pastor-body{display:flex;gap:26px}
.pastor .photo{width:280px;height:320px;background:linear-gradient(135deg,#9aa3a8,#6a6660 60%,#4a4440)}
.pastor blockquote{width:320px}
.pastor q{display:block;font-size:31px;line-height:1.2;margin-bottom:14px;quotes:"“" "”"}
.pastor blockquote p{font-size:15px;color:#bbb}
.pastor cite{display:block;font-style:normal;margin-top:14px;color:#aaa;font-size:14px}
.podcast{margin-left:60px;width:330px}
.podcast ul{list-style:none}
.podcast li{display:flex;gap:16px;margin-bottom:30px;font-size:15px;line-height:1.4}
.podcast li svg{flex:none}
.podcast li span{color:var(--grey)}

/* events */
.events{height:837px;padding:70px 70px 0 77px}
.events h2{text-align:center;font-size:40px;font-weight:500;color:#2a2a2a;letter-spacing:1px;margin-bottom:42px}
.event-row{display:flex;align-items:flex-start;height:210px;border-bottom:1px solid var(--line);padding-top:28px}
.event-row:last-child{border-bottom:none}
.date-box{width:180px;height:115px;background:#eeeeee;display:flex;align-items:center;gap:16px;padding-left:20px}
.date-box b{font-size:30px;font-weight:500;line-height:1}
.date-box b sup{font-size:15px}
.date-box small{display:block;font-size:17px}
.event-info{margin-left:70px;flex:1}
.event-info h4{font-size:20px;font-weight:600;margin-bottom:12px;color:#2a2a2a}
.event-info li{list-style:none;display:flex;align-items:center;gap:12px;font-size:15px;margin-bottom:6px}
.event-row .btn{margin-top:10px;padding:14px 30px}

/* dark footer */
.footer-main{height:524px;background:var(--darker);color:var(--white);display:flex;padding:80px 42px 0 42px;gap:50px}
.footer-main h5{font-size:19px;font-weight:500;margin-bottom:28px}
.f-col{width:330px}
.post{display:flex;gap:16px;margin-bottom:30px;font-size:15px;line-height:1.45}
.post .thumb{width:70px;height:70px;flex:none}
.post b{display:block;color:var(--blue);font-weight:500}
.post span{color:#bbb}
.tags{display:flex;flex-wrap:wrap;gap:10px;width:310px}
.tags span{background:var(--blue);font-size:14px;padding:6px 16px}
.feed{margin-top:60px;width:330px;height:170px;background:linear-gradient(135deg,#5b5b5b,#2b2b2b);display:flex;align-items:center;justify-content:center;font-size:22px}

/* light footer */
.footer-bottom{height:314px;display:flex;align-items:center;padding:0 42px 0 70px;position:relative}
.footer-bottom .brand{position:static;color:#333}
.footer-bottom .brand-name{font-size:50px}
.footer-bottom ul{list-style:none;display:flex;gap:24px;font-size:15px;font-weight:500;margin-left:auto;margin-right:22px;color:#333}
.footer-bottom .btn{padding:16px 22px}
.socials{position:absolute;left:150px;bottom:58px;display:flex;gap:10px}
.socials i{width:22px;height:22px;border:2px solid var(--grey);border-radius:50%}
.copyright{height:33px;background:#f3f3f3;text-align:center;font-size:11px;line-height:33px;color:#555;text-transform:uppercase}
</style>
</head>
<body>
<div class="page">

<header class="hero">
  <div class="hero-bg" role="img" aria-label="Photograph of a wooden cross in low dark light"></div>
  <nav class="topnav">
    <ul><li>HOME</li><li>TEAM</li><li>FEATURES</li><li>EVENTS</li><li>SERMONS</li><li>CONTACT</li><li>BLOG</li></ul>
    <a class="btn" href="#">Give Online</a>
  </nav>
  <div class="brand">
    <span class="brand-dot"></span>
    <div><div class="brand-name">WELLSPRING</div><div class="brand-sub">GRACE CHURCH</div></div>
  </div>
  <div class="service-times"><span>Sunday Worship 10:15</span><span>Sunday School 09:00</span></div>
  <div class="hero-copy">
    <p class="hero-kicker">A very special celebration this year</p>
    <h1 class="hero-title">EASTER WEEK</h1>
    <div class="hero-rule"></div>
    <p class="hero-sub">JOIN THE REMEMBERANCE</p>
    <p class="hero-time">Service starting at 19:00 daily</p>
    <a class="btn" href="#">Continue Reading</a>
  </div>
</header>

<div class="visitor-bar">
  <p>First time visitor? Find out how, where and when we worship. We hope to see you soon.</p>
  <a class="btn" href="#">Visitors Info</a>
</div>

<section class="welcome">
  <div class="welcome-text">
    <h2>WELCOME TO</h2>
    <h3>WELLSPRING GRACE CHURCH</h3>
    <p>Lorem ipsum dolor sit amet, consectetur adipiscing elit, sed do eius mod tempor incididunt ut labore et dolore magna aliqua. Ut enim ad minim veniam, quis nostrud exercitation ulla co laboris nisi ut aliquip ex ea commodo consequat.</p>
    <p>Duis aute irure dolor in reprehenderit in voluptate velit esse cillum dolore eu fugiat nulla pariatur.</p>
    <span class="signature">Pastor Daniel</span>
  </div>
  <div class="photo" role="img" aria-label="Black and white photograph of an elderly couple embracing"></div>
</section>

<section class="countdown" aria-label="Next event">
  <div>
    <div class="event-head">
      <svg width="58" height="58" viewBox="0 0 58 58" fill="none" stroke="var(--blue)" stroke-width="4"><rect x="4" y="9" width="50" height="45" rx="3"/><path d="M4 20h50M16 3v11M42 3v11"/><path d="M19 37l7 7 14-14"/></svg>
      <div><h4>Church leaders meeting</h4><p class="date">March 27, 2019 - 07:00 pm</p></div>
    </div>
    <p class="event-note">Meeting for the church leaders. This is where we plan the strategy for the church and give feedback on projects.</p>
  </div>
  <div class="timer">
    <div class="timer-cells">
      <div><small>Days</small><b>06</b></div>
      <div><small>Hours</small><b>15</b></div>
      <div><small>Minutes</small><b>26</b></div>
      <div><small>Seconds</small><b>16</b></div>
    </div>
    <a class="btn" href="#">Read More</a>
  </div>
</section>

<section class="features">
  <div class="feature">
    <svg viewBox="0 0 60 72" width="60" fill="none" stroke="var(--ink)" stroke-width="3"><path d="M30 2v14M24 8h12"/><path d="M14 34L30 18l16 16"/><path d="M14 34v36h32V34"/><path d="M2 70h56M4 70V48l10-8M56 70V48l-10-8"/><path d="M25 70V56a5 5 0 0110 0v14"/></svg>
    <h5>What we believe</h5>
    <p>We believe in the existence of GOD and His Holy Word to be the foundation of our faith. It shall not be moved nor be compromised.</p>
  </div>
  <div class="feature">
    <svg viewBox="0 0 64 72" width="64" fill="none" stroke="var(--ink)" stroke-width="3"><path d="M31 6c-4 8-10 18-12 30l-9 16 10 16 11-10V6z"/><path d="M33 6c4 8 10 18 12 30l9 16-10 16-11-10V6z"/></svg>
    <h5>Services &amp; Locations</h5>
    <p>Riverside, OH 45011, USA<br>Sunday morning (08:15 - 12:00 PM)<br>Sunday afternoon (04:00 - 06:00 PM)<br>Wednesday (08:00 - 09:00 PM)</p>
  </div>
  <div class="feature">
    <svg viewBox="0 0 78 72" width="78" fill="none" stroke="var(--ink)" stroke-width="3"><rect x="3" y="6" width="72" height="46" rx="3"/><path d="M3 44h72M32 52l-4 14M46 52l4 14M22 66h34"/></svg>
    <h5>Watch Live</h5>
    <p>By God's grace, we are glad to deliver an online live streaming just for you. Join us by watching live every Sunday and Wednesday.</p>
  </div>
</section>

<section class="involved">
  <div class="mosaic">
    <div class="tile t-kids" role="img" aria-label="Photograph of children at a ministry activity"><span>Kids Ministry</span></div>
    <div class="tile t-out" role="img" aria-label="Photograph of volunteers on an outreach"><span>Outreach</span></div>
    <div class="tile t-teen" role="img" aria-label="Photograph of teenagers in a group"><span>Teens Ministry</span></div>
    <div class="tile t-senior" role="img" aria-label="Photograph of seniors gathered together"><span>Seniors Ministry</span></div>
    <div class="tile t-bible" role="img" aria-label="Photograph of an open bible"><span>Bible Study</span></div>
  </div>
  <div class="involved-text">
    <h2>GET INVOLVED</h2>
    <p>The success of our church depends on participation from people like you. Get involved in our ministries, it will change your life.</p>
  </div>
</section>

<section class="blog">
  <div class="blog-text">
    <h2>LATEST BLOG</h2>
    <time>Jan 31, 2019</time>
    <h4>Pray without ceasing</h4>
    <p>Lorem ipsum dolor sit amet, consectetur adipiscing elit, sed do eiusmod tempor incididunt ut labore et dolore magna aliqua. Ut enim ad minim veniam, quis nostrud exercitation ullamcolaboris nisi ut aliquip ex ea comm odo consequ.</p>
    <a class="btn" href="#">Read More</a>
  </div>
  <div class="photo" role="img" aria-label="Silhouette of a person praying against a sunset"></div>
</section>

<section class="pastor">
  <div class="pastor-col">
    <h3 class="label">Pastor</h3>
    <div class="pastor-body">
      <div class="photo" role="img" aria-label="Portrait photograph of the pastor"></div>
      <blockquote>
        <q>One thing I asked of the Lord</q>
        <p>Lorem ipsum dolor sit amet, con sectetur adipiscing elit, sed tem uismod tempor incididunt ut lab ore et dolore magna aliqua. Ut enim ad minim veniam, quis nos trud exercitation ullamco.</p>
        <cite>— Daniel Ashford —</cite>
      </blockquote>
    </div>
  </div>
  <div class="podcast">
    <h3 class="label">Podcast</h3>
    <ul>
      <li><svg width="26" height="26" viewBox="0 0 26 26"><rect x="1" y="1" width="24" height="24" fill="none" stroke="#fff" stroke-width="1.5"/><path d="M10 7l8 6-8 6z" fill="#fff"/></svg><p>Holy Spirit : Strategy Thinking<br><span>by Daniel Ashford</span></p></li>
      <li><svg width="26" height="26" viewBox="0 0 26 26"><rect x="1" y="1" width="24" height="24" fill="none" stroke="#fff" stroke-width="1.5"/><path d="M10 7l8 6-8 6z" fill="#fff"/></svg><p>Holy Spirit : Strategy Thinking<br><span>by Daniel Ashford</span></p></li>
      <li><svg width="26" height="26" viewBox="0 0 26 26"><rect x="1" y="1" width="24" height="24" fill="none" stroke="#fff" stroke-width="1.5"/><path d="M10 7l8 6-8 6z" fill="#fff"/></svg><p>Holy Spirit : Strategy Thinking<br><span>by Daniel Ashford</span></p></li>
    </ul>
  </div>
</section>

<section class="events">
  <h2>UPCOMING EVENTS</h2>
  <div class="event-row">
    <div class="date-box"><svg width="40" height="40" viewBox="0 0 40 40" fill="none" stroke="var(--ink)" stroke-width="2.5"><rect x="3" y="6" width="34" height="31"/><path d="M3 14h34M11 2v8M29 2v8M10 21h4M18 21h4M26 21h4M10 28h4M18 28h4M26 28h4"/></svg><div><b>22<sup>nd</sup></b><small>Feb 2019</small></div></div>
    <div class="event-info"><h4>Sharing our faith and love to children</h4><ul>
      <li><svg width="14" height="14" viewBox="0 0 14 14" fill="none" stroke="var(--ink)" stroke-width="1.5"><circle cx="7" cy="7" r="6"/><path d="M7 3v4l3 2"/></svg>Thursday 08:00 - 09:00 am</li>
      <li><svg width="14" height="14" viewBox="0 0 14 14" fill="none" stroke="var(--ink)" stroke-width="1.5"><path d="M7 13S2 8 2 5a5 5 0 0110 0c0 3-5 8-5 8z"/><circle cx="7" cy="5" r="1.6"/></svg>Wellspring Grace Church</li>
      <li><svg width="14" height="14" viewBox="0 0 14 14" fill="none" stroke="var(--ink)" stroke-width="1.5"><path d="M1 6l12-5-5 12-2-5z"/></svg>Elm Park, Riverside OH 45011</li></ul></div>
    <a class="btn" href="#">Read More</a>
  </div>
  <div class="event-row">
    <div class="date-box"><svg width="40" height="40" viewBox="0 0 40 40" fill="none" stroke="var(--ink)" stroke-width="2.5"><rect x="3" y="6" width="34" height="31"/><path d="M3 14h34M11 2v8M29 2v8M10 21h4M18 21h4M26 21h4M10 28h4M18 28h4M26 28h4"/></svg><div><b>18<sup>th</sup></b><small>Feb 2019</small></div></div>
    <div class="event-info"><h4>Know Jesus Christ better through lines</h4><ul>
      <li><svg width="14" height="14" viewBox="0 0 14 14" fill="none" stroke="var(--ink)" stroke-width="1.5"><circle cx="7" cy="7" r="6"/><path d="M7 3v4l3 2"/></svg>Thursday 08:00 - 09:00 am</li>
      <li><svg width="14" height="14" viewBox="0 0 14 14" fill="none" stroke="var(--ink)" stroke-width="1.5"><path d="M7 13S2 8 2 5a5 5 0 0110 0c0 3-5 8-5 8z"/><circle cx="7" cy="5" r="1.6"/></svg>Wellspring Grace Church</li>
      <li><svg width="14" height="14" viewBox="0 0 14 14" fill="none" stroke="var(--ink)" stroke-width="1.5"><path d="M1 6l12-5-5 12-2-5z"/></svg>Elm Park, Riverside OH 45011</li></ul></div>
    <a class="btn" href="#">Read More</a>
  </div>
  <div class="event-row">
    <div class="date-box"><svg width="40" height="40" viewBox="0 0 40 40" fill="none" stroke="var(--ink)" stroke-width="2.5"><rect x="3" y="6" width="34" height="31"/><path d="M3 14h34M11 2v8M29 2v8M10 21h4M18 21h4M26 21h4M10 28h4M18 28h4M26 28h4"/></svg><div><b>12<sup>th</sup></b><small>Feb 2019</small></div></div>
    <div class="event-info"><h4>Caring about the community and serving</h4><ul>
      <li><svg width="14" height="14" viewBox="0 0 14 14" fill="none" stroke="var(--ink)" stroke-width="1.5"><circle cx="7" cy="7" r="6"/><path d="M7 3v4l3 2"/></svg>Thursday 08:00 - 09:00 am</li>
      <li><svg width="14" height="14" viewBox="0 0 14 14" fill="none" stroke="var(--ink)" stroke-width="1.5"><path d="M7 13S2 8 2 5a5 5 0 0110 0c0 3-5 8-5 8z"/><circle cx="7" cy="5" r="1.6"/></svg>Wellspring Grace Church</li>
      <li><svg width="14" height="14" viewBox="0 0 14 14" fill="none" stroke="var(--ink)" stroke-width="1.5"><path d="M1 6l12-5-5 12-2-5z"/></svg>Elm Park, Riverside OH 45011</li></ul></div>
    <a class="btn" href="#">Read More</a>
  </div>
</section>

<footer>
  <div class="footer-main">
    <div class="f-col">
      <h5>Latest Sermons</h5>
      <div class="post"><div class="thumb" role="img" aria-label="Photograph of a person outdoors" style="background:linear-gradient(135deg,#6f8a5a,#2f3d28)"></div><p><b>All things are possible</b><span>Lorem ipsum dolor sit amet, consectetur.</span></p></div>
      <div class="post"><div class="thumb" role="img" aria-label="Photograph of a cross at dusk" style="background:linear-gradient(135deg,#8a8a8a,#2e2e2e)"></div><p><b>Abounding the work of Lord</b><span>Lorem ipsum dolor sit amet, consectetur.</span></p></div>
    </div>
    <div class="f-col">
      <h5>Sermons Tags</h5>
      <div class="tags"><span>Faith</span><span>Forgiveness</span><span>Goodheartedness</span><span>Kindness</span><span>Love</span><span>Peace</span><span>Understanding</span></div>
      <div class="feed" role="img" aria-label="Photograph of a microphone behind a feed label">Audio Feed</div>
    </div>
    <div class="f-col">
      <h5>Latest News</h5>
      <div class="post"><div class="thumb" role="img" aria-label="Photograph of a congregation" style="background:linear-gradient(135deg,#7b7b8c,#2c2c38)"></div><p><b>Holy Spirit</b><span>Lorem ipsum dolor sit amet, consectetur.</span></p></div>
      <div class="post"><div class="thumb" role="img" aria-label="Photograph of candles in a church" style="background:linear-gradient(135deg,#c9a45a,#3a2a16)"></div><p><b>Holy Spirit</b><span>Lorem ipsum dolor sit amet, consectetur.</span></p></div>
    </div>
  </div>
  <div class="footer-bottom">
    <div class="brand">
      <span class="brand-dot"></span>
      <div><div class="brand-name">WELLSPRING</div><div class="brand-sub">GRACE CHURCH</div></div>
    </div>
    <ul><li>HOME</li><li>TEAM</li><li>FEATURES</li><li>EVENTS</li><li>SERMONS</li><li>CONTACT</li><li>BLOG</li></ul>
    <a class="btn" href="#">Give Online</a>
    <div class="socials"><i></i><i></i><i></i></div>
  </div>
  <div class="copyright">Copyright © 2019 Wellspring Grace Church. All rights reserved.</div>
</footer>

</div>
</body>
</html>
```